I need a direct mail postcard made up for my marketing campaign

I am starting a marketing campaign and need a design for a post card. I own an iron door company and need to have before and after images on the post card to showcase what our work looks like. I have provided pictures to use below.

The design needs to be two sided. The logo should be on the front.

The tag line for this campaign is: Design the smile your home deserves.

Words to also use: Distinctive style, Work of Art, One-of-a-Kind, Elegant, Modern, Innovative, Unique

My information for the card
Name: Dean Harlowe
Phone number: (555)-318-2764
Email: Dean@wroughtgatestudio.example

The US postal system is very picky as to what can be sent in the mail. The only requirement they have is for the address. There needs to be a 2inch (50.8mm) by 4inch (101.6mm) blank space on the bottom right hand corner on the back of the card.

Target Market(s)

Home owners

Industry/Entity Type

Home Improvement

Font styles to use
Serif
Decorative

Colors
0555a3
ffffff
ec1f27

Requirements
Must have
• My logo, My contact information, before and after pictures
• Provided 3D images
Nice to have
• Words that describe iron doors
• A contrast between contemporary and ornate doors.

```html
<!DOCTYPE html>
<html lang="en">
<head>
<meta charset="utf-8">
<title>Wrought Gate Studio – Postcard</title>
<link rel="stylesheet" href="https://fonts.googleapis.com/css2?family=Montserrat:wght@400;600;800&family=Oswald:wght@300;400;600&display=swap">
<style>
  :root {
    --blue: #434c9e;
    --red: #c8323e;
    --white: #ffffff;
    --ink: #2b2b2b;
    --body: #555555;
    --line: #b9b9b9;
    --page: #ecebe8;
  }
  * { box-sizing: border-box; margin: 0; padding: 0; }
  html, body { width: 909px; height: 1200px; overflow: hidden; }
  body { background: var(--page); position: relative; font-family: "Oswald", sans-serif; }

  .card {
    position: absolute; left: 67px; width: 771px; height: 496px;
    background: var(--white); overflow: hidden;
    box-shadow: 0 2px 8px rgba(0,0,0,.18);
  }
  .card--front { top: 67px; }
  .card--back { top: 624px; }

  /* Front */
  .top-band { position: absolute; left: 0; top: 0; width: 100%; height: 111px; background: var(--blue); }
  .logo-box {
    position: absolute; left: 35px; top: 26px; width: 156px; height: 153px;
    background: var(--white); padding: 10px 12px;
  }
  .logo-frame {
    width: 100%; height: 100%; border: 1px solid var(--blue);
    display: flex; align-items: center; justify-content: center; text-align: center;
    font-family: "Montserrat", sans-serif; font-weight: 800; color: var(--blue);
    font-size: 15px; line-height: 1.25; letter-spacing: .5px; text-transform: uppercase;
  }
  .campaign-title {
    position: absolute; left: 371px; top: 29px; width: 343px; height: 64px;
    border: 1.5px solid var(--white);
    display: flex; align-items: center; justify-content: center;
    font-family: "Montserrat", sans-serif; font-weight: 800; font-size: 36px; color: var(--white);
  }
  .intro { position: absolute; left: 27px; top: 197px; width: 306px; }
  .tagline { font-weight: 600; font-size: 21px; color: var(--red); letter-spacing: -.3px; line-height: 1.2; }
  .subline { font-weight: 400; font-size: 15px; color: var(--ink); margin-top: 5px; letter-spacing: -.2px; }
  .intro-copy { font-weight: 300; font-size: 14.5px; line-height: 19px; color: var(--body); margin-top: 6px; text-align: justify; letter-spacing: -.2px; }

  .web-band {
    position: absolute; left: 0; top: 395px; width: 100%; height: 28px; background: var(--blue);
    color: var(--white); font-family: "Montserrat", sans-serif; font-size: 13.5px; letter-spacing: 1.2px;
    padding-left: 27px; line-height: 28px;
  }
  .call-band {
    position: absolute; left: 0; top: 423px; width: 100%; height: 73px; background: var(--red);
    color: var(--white); font-weight: 600; font-size: 36px; padding-left: 27px; line-height: 70px;
  }
  .showcase {
    position: absolute; left: 359px; top: 108px; width: 369px; height: 350px;
    background: var(--white); box-shadow: 0 8px 14px rgba(0,0,0,.15);
  }
  .showcase-photo { position: absolute; top: 11px; height: 328px; }
  .showcase-photo--before { left: 12px; width: 137px; background: linear-gradient(180deg, #3a2d1e 0 23%, #eceae4 23% 100%); }
  .showcase-photo--after { left: 161px; width: 194px; background: linear-gradient(180deg, #e9e2d4 0%, #4a4257 18%, #3b3446 100%); }
  .photo-label {
    position: absolute; top: 2px; font-family: "Montserrat", sans-serif; font-style: italic; font-weight: 600;
    font-size: 12px; color: var(--white);
  }
  .showcase-photo--before .photo-label { left: 3px; }
  .showcase-photo--after .photo-label { right: 4px; }

  /* Back */
  .gallery-photo { position: absolute; }
  .gallery-photo--entry { left: 14px; top: 22px; width: 202px; height: 99px; background: linear-gradient(90deg, #a08a6c, #5a4a3a 45%, #2a2a33); }
  .gallery-photo--modern-a { left: 222px; top: 32px; width: 76px; height: 104px; background: linear-gradient(180deg, #ededed, #d8d8d8); }
  .gallery-photo--modern-b { left: 305px; top: 32px; width: 76px; height: 104px; background: linear-gradient(180deg, #ededed, #d8d8d8); }
  .features { position: absolute; left: 20px; top: 153px; width: 362px; }
  .features-title { font-weight: 600; font-size: 20px; color: var(--red); letter-spacing: -.3px; }
  .features-copy { font-weight: 300; font-size: 14.5px; line-height: 19px; color: var(--body); margin-top: 6px; letter-spacing: -.2px; }

  .contact-band { position: absolute; left: 14px; top: 285px; width: 371px; height: 136px; background: var(--red); }
  .portrait {
    position: absolute; left: 29px; top: 256px; width: 127px; height: 155px;
    border: 2px solid var(--white); background: linear-gradient(180deg, #b8c3cc 0%, #8e9aa6 55%, #2a2f3a 100%);
  }
  .contact-name { position: absolute; left: 172px; top: 314px; font-weight: 600; font-size: 27px; color: var(--white); letter-spacing: -.4px; }
  .contact-line {
    position: absolute; left: 178px; display: flex; align-items: center; gap: 5px;
    color: var(--white); font-family: "Montserrat", sans-serif;
  }
  .contact-line--phone { top: 360px; font-size: 14px; }
  .contact-line--email { top: 385px; font-size: 10.5px; }
  .contact-line svg { fill: var(--white); }
  .web-bar {
    position: absolute; left: 14px; top: 428px; width: 371px; height: 49px; background: var(--blue);
    color: var(--white); font-family: "Montserrat", sans-serif; font-size: 18px; letter-spacing: .6px;
    line-height: 49px; padding-left: 17px;
  }

  .return-address { position: absolute; left: 452px; top: 33px; font-family: "Montserrat", sans-serif; font-size: 11.5px; line-height: 15.5px; color: #666; }
  .stamp-box { position: absolute; left: 662px; top: 28px; width: 84px; height: 80px; border: 1px solid #9a9a9a; }
  .address-line { position: absolute; left: 484px; width: 261px; height: 1px; background: var(--line); }
</style>
</head>
<body>

  <section class="card card--front">
    <div class="top-band"></div>
    <div class="logo-box"><div class="logo-frame">Wrought<br>Gate<br>Studio</div></div>
    <h1 class="campaign-title">Distinctive style</h1>

    <div class="intro">
      <h2 class="tagline">Design the smile your home deserves</h2>
      <p class="subline">Where superior quality meets beautiful elegance</p>
      <p class="intro-copy">Our doors represent unique works of art, handmade for you and your home. Wrought Gate Studio doors have a one-of-a-kind distinction and provide the ultimate in first impressions and curb appeal. We take pride in manufacturing for our customer an awe-inspiring design that will enhance the beauty and value of your home.</p>
    </div>

    <div class="web-band">www.wroughtgatestudio.example</div>
    <div class="call-band">Call: (555)-318-2764</div>

    <div class="showcase">
      <div class="showcase-photo showcase-photo--before" role="img" aria-label="Before: plain white paneled double front door under an arched transom window">
        <span class="photo-label">before</span>
      </div>
      <div class="showcase-photo showcase-photo--after" role="img" aria-label="After: arched dark iron double door with scrollwork and holiday wreaths">
        <span class="photo-label">after</span>
      </div>
    </div>
  </section>

  <section class="card card--back">
    <div class="gallery-photo gallery-photo--entry" role="img" aria-label="Stone home entry with an ornate iron door"></div>
    <div class="gallery-photo gallery-photo--modern-a" role="img" aria-label="Contemporary bronze iron door with curved glass panels"></div>
    <div class="gallery-photo gallery-photo--modern-b" role="img" aria-label="Contemporary bronze iron door with horizontal glass slats"></div>

    <div class="features">
      <h2 class="features-title">Modern, Innovative, Unique...</h2>
      <p class="features-copy">Meet with our design staff to customize an iron door, or select from one of our sophisticated in-stock doors to make that statement of exclusive elegance that you and your home deserve.</p>
    </div>

    <div class="contact-band"></div>
    <div class="portrait" role="img" aria-label="Portrait photo of the sales representative in a suit"></div>
    <p class="contact-name">Dean Harlowe</p>
    <p class="contact-line contact-line--phone">
      <svg width="12" height="12" viewBox="0 0 24 24" aria-hidden="true"><path d="M6.6 10.8a15.1 15.1 0 0 0 6.6 6.6l2.2-2.2c.3-.3.7-.4 1-.2 1.1.4 2.3.6 3.6.6.6 0 1 .4 1 1V20c0 .6-.4 1-1 1A17 17 0 0 1 3 4c0-.6.4-1 1-1h3.5c.6 0 1 .4 1 1 0 1.3.2 2.5.6 3.6.1.3 0 .7-.2 1l-2.3 2.2z"/></svg>
      (555)-318-2764
    </p>
    <p class="contact-line contact-line--email">
      <svg width="12" height="9" viewBox="0 0 24 18" aria-hidden="true"><path d="M0 0h24v18H0z M2 2v.6l10 6.5 10-6.5V2z" fill-rule="evenodd"/></svg>
      Dean@wroughtgatestudio.example
    </p>
    <div class="web-bar">www.wroughtgatestudio.example</div>

    <p class="return-address">4820 Alder Crest Lane,<br>Millbrook Point,<br>FL 30000</p>
    <div class="stamp-box"></div>
    <div class="address-line" style="top:201px"></div>
    <div class="address-line" style="top:238px"></div>
    <div class="address-line" style="top:275px"></div>
    <div class="address-line" style="top:312px"></div>
  </section>

</body>
</html>
```